Design a business Card

Design a business card (front and back) for a Technology Consulting firm. Preference is for a clean look - professional, favour minimalist rather than something busy. two logos are attached. You can use any of them. . The information below is for the purpose of presenting an entry in the contest, but the winner will be given correct information to product another version of the entry. The winner will also be given an opportunity to prepare a letterhead (ideally consistent with the business card).

Carla Wendover
Partner
+61 438 926 417
+61 7 3890 2615
jane@[url removed, login to view]
[url removed, login to view]
GPO Box 6093
Brisbane QLD 4009

The winning entry should be in a format that most business card printers can easily print.

```html
<!DOCTYPE html>
<html lang="en">
<head>
<meta charset="utf-8">
<title>Norvane Business Card</title>
<link href="https://fonts.googleapis.com/css2?family=Ubuntu:wght@400;500;700&display=swap" rel="stylesheet">
<style>
  :root {
    --page: #e9eaec;
    --card-white: #ffffff;
    --charcoal: #262626;
    --brand-blue: #1b8fd6;
    --text-light: #f2f2f2;
    --text-grey: #5a5a5a;
  }
  * { margin: 0; padding: 0; box-sizing: border-box; }
  html, body {
    width: 1200px;
    height: 900px;
    overflow: hidden;
    background: var(--page);
    font-family: "Ubuntu", sans-serif;
  }
  .canvas {
    position: relative;
    width: 1200px;
    height: 900px;
  }
  .card {
    position: absolute;
    left: 320px;
    width: 560px;
    height: 320px;
    border-radius: 22px;
    overflow: hidden;
    box-shadow: 0 8px 24px rgba(0,0,0,0.12);
  }
  /* Front */
  .card-front {
    top: 100px;
    background: var(--card-white);
    display: flex;
    align-items: center;
    justify-content: center;
  }
  .front-wordmark {
    font-weight: 700;
    font-size: 64px;
    letter-spacing: 2px;
    color: var(--brand-blue);
  }
  /* Back */
  .card-back {
    top: 480px;
    background: var(--charcoal);
  }
  .back-brand-strip {
    position: absolute;
    left: 0; top: 0;
    width: 150px;
    height: 302px;
    background: var(--card-white);
  }
  .brand-lockup {
    position: absolute;
    left: 75px;
    top: 151px;
    width: 260px;
    transform: translate(-50%, -50%) rotate(-90deg);
    display: flex;
    align-items: center;
    gap: 10px;
  }
  .brand-name {
    font-weight: 700;
    font-size: 30px;
    color: var(--brand-blue);
  }
  .brand-divider {
    width: 2px;
    height: 42px;
    background: var(--text-grey);
  }
  .brand-descriptor {
    display: flex;
    flex-direction: column;
    color: var(--text-grey);
    line-height: 1.1;
  }
  .brand-descriptor .line {
    font-size: 12px;
    font-weight: 500;
    letter-spacing: 1px;
    text-transform: uppercase;
  }
  .brand-descriptor .tagline {
    font-size: 7px;
    letter-spacing: 1px;
    text-transform: uppercase;
    margin-top: 2px;
  }
  .blue-band {
    position: absolute;
    left: 0; bottom: 0;
    width: 100%;
    height: 18px;
    background: var(--brand-blue);
  }
  .name-plate {
    position: absolute;
    top: 24px;
    right: 0;
    width: 190px;
    height: 56px;
    background: var(--card-white);
    padding: 8px 14px 0 0;
    text-align: right;
  }
  .person-name {
    font-size: 18px;
    font-weight: 500;
    color: var(--brand-blue);
    line-height: 1.2;
  }
  .person-role {
    font-size: 13px;
    color: var(--text-grey);
  }
  .contact-list {
    position: absolute;
    left: 200px;
    top: 128px;
    list-style: none;
    color: var(--text-light);
    font-size: 13px;
  }
  .contact-list li {
    display: flex;
    align-items: center;
    gap: 10px;
    height: 26px;
  }
  .contact-icon {
    width: 11px;
    height: 11px;
    fill: var(--brand-blue);
    flex: none;
  }
</style>
</head>
<body>
<main class="canvas">
  <section class="card card-front" aria-label="Card front">
    <span class="front-wordmark">Norvane</span>
  </section>

  <section class="card card-back" aria-label="Card back">
    <div class="back-brand-strip">
      <div class="brand-lockup">
        <span class="brand-name">Norvane</span>
        <span class="brand-divider"></span>
        <span class="brand-descriptor">
          <span class="line">Consulting</span>
          <span class="line">Services Ltd</span>
          <span class="tagline">Smart Tech Advice</span>
        </span>
      </div>
    </div>

    <div class="name-plate">
      <div class="person-name">Carla Wendover</div>
      <div class="person-role">Partner</div>
    </div>

    <ul class="contact-list">
      <li>
        <svg class="contact-icon" viewBox="0 0 24 24" aria-hidden="true"><path d="M6.6 10.8a15.1 15.1 0 0 0 6.6 6.6l2.2-2.2a1 1 0 0 1 1-.25 11.4 11.4 0 0 0 3.6.57 1 1 0 0 1 1 1V20a1 1 0 0 1-1 1A17 17 0 0 1 3 4a1 1 0 0 1 1-1h3.5a1 1 0 0 1 1 1c0 1.25.2 2.45.57 3.6a1 1 0 0 1-.25 1z"/></svg>
        <span>+61 438 926 417 , +61 7 3890 2615</span>
      </li>
      <li>
        <svg class="contact-icon" viewBox="0 0 24 24" aria-hidden="true"><path d="M2 5h20v14H2z M2 5l10 8 10-8" fill="none" stroke="#1b8fd6" stroke-width="2.4"/></svg>
        <span>carla@norvanetech.com</span>
      </li>
      <li>
        <svg class="contact-icon" viewBox="0 0 24 24" aria-hidden="true"><circle cx="12" cy="12" r="9.5" fill="none" stroke="#1b8fd6" stroke-width="2.4"/><path d="M2.5 12h19M12 2.5c3 3 3 16 0 19M12 2.5c-3 3-3 16 0 19" fill="none" stroke="#1b8fd6" stroke-width="2"/></svg>
        <span>www.norvanetech.com</span>
      </li>
      <li>
        <svg class="contact-icon" viewBox="0 0 24 24" aria-hidden="true"><path d="M12 2a7 7 0 0 0-7 7c0 5.2 7 13 7 13s7-7.8 7-13a7 7 0 0 0-7-7zm0 9.5A2.5 2.5 0 1 1 12 6.5a2.5 2.5 0 0 1 0 5z"/></svg>
        <span>GPO Box 6093 , Brisbane QLD 4009</span>
      </li>
    </ul>

    <div class="blue-band"></div>
  </section>
</main>
</body>
</html>
```